Branvique needs a business Card Design

We are looking for a business card Design for our new Managed Service Provider Company, Branvique. Branvique encompasses everything IT for the average medium sized business. Our primary services are help desk support, cyber-security (malware and ransomware protection), and Disaster Recovery systems. We would like the design to have a very clean and professional look, with a very minimalist feel.

Target Market(s)

Medium to large sized businesses

Industry/Entity Type

It Service

Contact Information for Business Card

Name GoesHere
name@branvique.com
O: 555-382-6047
C: 555-731-5820

Font styles to use
Other font styles liked:
• Poppins Font Only Please

Colors

Designer to choose only greyscale colors for use in the design.

Requirements
Must have
• Logo included
Nice to have
• Cutting Edge, innovative, minimalistic, elegant

```html
<!DOCTYPE html>
<html lang="en">
<head>
<meta charset="utf-8">
<title>Branvique — Business Card</title>
<link rel="stylesheet" href="https://fonts.googleapis.com/css2?family=Poppins:wght@300;400;600&family=Montserrat:wght@700&display=swap">
<style>
  :root {
    --backdrop: #b4b4b4;
    --card-white: #f7f7f7;
    --navy-deep: #123b63;
    --navy-mid: #1c4f7e;
    --ink: #1a2a44;
    --ink-soft: #4b5566;
    --accent-red: #d8321f;
    --on-navy: #ffffff;
    --on-navy-soft: rgba(255,255,255,0.78);
  }
  * { box-sizing: border-box; margin: 0; padding: 0; }
  html, body { width: 1200px; height: 914px; overflow: hidden; }
  body {
    background: var(--backdrop);
    font-family: "Poppins", sans-serif;
    display: flex;
    align-items: center;
    justify-content: center;
    gap: 80px;
  }
  .card {
    position: relative;
    width: 320px;
    height: 560px;
    overflow: hidden;
    box-shadow: 0 10px 30px rgba(0,0,0,0.18);
  }
  .card-art { position: absolute; inset: 0; }
  .card--back { background: var(--card-white); }
  .card--back .card-art {
    background: linear-gradient(180deg, #fbfbfb 0%, #f0f0f0 55%, #e6e6e6 100%);
  }
  .card--front { background: var(--navy-deep); }
  .card--front .card-art {
    background: linear-gradient(170deg, var(--navy-mid) 0%, var(--navy-deep) 60%, #0f3255 100%);
  }
  .card-content {
    position: relative;
    height: 100%;
    display: flex;
    flex-direction: column;
    align-items: center;
  }
  .brand {
    display: flex;
    align-items: center;
    gap: 10px;
    font-weight: 400;
    letter-spacing: 0.32em;
    text-transform: uppercase;
  }
  .brand-dot {
    width: 10px;
    height: 10px;
    border-radius: 50%;
    background: currentColor;
  }
  .card--back .brand {
    margin-top: 92px;
    font-size: 22px;
    color: var(--ink);
  }
  .contact-list {
    list-style: none;
    margin-top: 56px;
    display: flex;
    flex-direction: column;
    align-items: center;
    gap: 6px;
    color: var(--ink-soft);
    font-size: 13px;
    font-weight: 300;
  }
  .contact-item {
    display: flex;
    flex-direction: column;
    align-items: center;
    gap: 4px;
  }
  .contact-icon { width: 16px; height: 16px; }
  .card--front .brand {
    margin-top: 200px;
    font-size: 26px;
    color: var(--on-navy);
  }
  .brand-rule {
    width: 120px;
    height: 1px;
    background: var(--on-navy-soft);
    margin-top: 14px;
  }
  .tagline {
    margin-top: 6px;
    font-size: 10.5px;
    font-weight: 300;
    letter-spacing: 0.02em;
    color: var(--on-navy-soft);
    text-transform: uppercase;
  }
  .person-name {
    margin-top: 120px;
    font-family: "Montserrat", sans-serif;
    font-weight: 700;
    font-size: 20px;
    color: var(--on-navy);
  }
  .person-title {
    margin-top: 2px;
    font-size: 14px;
    color: var(--on-navy);
  }
</style>
</head>
<body>
  <section class="card card--back">
    <div class="card-art" role="img" aria-label="Faint city map and building photograph in pale grey"></div>
    <div class="card-content">
      <div class="brand"><span class="brand-dot"></span>Branvique</div>
      <ul class="contact-list">
        <li class="contact-item">418 Larch Ct, Fairview, Ohio
          <svg class="contact-icon" viewBox="0 0 16 16" aria-hidden="true"><circle cx="8" cy="8" r="8" fill="var(--accent-red)"/><path d="M8 3.5a2.6 2.6 0 0 0-2.6 2.6C5.4 8 8 11.5 8 11.5s2.6-3.5 2.6-5.4A2.6 2.6 0 0 0 8 3.5z" fill="#fff"/><circle cx="8" cy="6.1" r="0.9" fill="var(--accent-red)"/></svg>
        </li>
        <li class="contact-item">+555-382-6047
          <svg class="contact-icon" viewBox="0 0 16 16" aria-hidden="true"><circle cx="8" cy="8" r="8" fill="var(--accent-red)"/><rect x="4" y="5.5" width="8" height="5.5" rx="1" fill="#fff"/></svg>
        </li>
        <li class="contact-item">+555-731-5820
          <svg class="contact-icon" viewBox="0 0 16 16" aria-hidden="true"><circle cx="8" cy="8" r="8" fill="var(--accent-red)"/><rect x="5.8" y="3.5" width="4.4" height="9" rx="0.8" fill="#fff"/></svg>
        </li>
        <li class="contact-item">name@branvique.com
          <svg class="contact-icon" viewBox="0 0 16 16" aria-hidden="true"><circle cx="8" cy="8" r="8" fill="var(--accent-red)"/><rect x="4" y="5" width="8" height="6" rx="0.8" fill="#fff"/><path d="M4 5.3 8 8.5 12 5.3" fill="none" stroke="var(--accent-red)" stroke-width="0.8"/></svg>
        </li>
        <li class="contact-item">www.branvique.com
          <svg class="contact-icon" viewBox="0 0 16 16" aria-hidden="true"><circle cx="8" cy="8" r="8" fill="var(--accent-red)"/><circle cx="8" cy="8" r="4" fill="none" stroke="#fff" stroke-width="0.9"/><path d="M4 8h8M8 4c-1.8 2.4-1.8 5.6 0 8M8 4c1.8 2.4 1.8 5.6 0 8" fill="none" stroke="#fff" stroke-width="0.8"/></svg>
        </li>
      </ul>
    </div>
  </section>

  <section class="card card--front">
    <div class="card-art" role="img" aria-label="Dim navy-toned photograph of a high-rise building"></div>
    <div class="card-content">
      <div class="brand"><span class="brand-dot"></span>Branvique</div>
      <div class="brand-rule"></div>
      <p class="tagline">Complete IT Service Partners</p>
      <p class="person-name">John Doe</p>
      <p class="person-title">Co-Founder | Partner</p>
    </div>
  </section>
</body>
</html>
```